Homemaking training schools needs a Business Card design

Designer, Hello!

No special requirements, good-looking enough.
--------------------------------------------------------------------------

Name: Marcus Liao
Chairman
Tel: 0574-57418263
Mobile: 13852247106
Email: kelvory@mailpond.com
Web: www.tqb2031.com
Add: No.258, LinfengJie, DaoyueQu, Ningbo, Zhejiang

LOGO
Ningbo TQB Homemaking Training School

Target Market(s)

pregnant women, mothers, infants, the elderly and families, including cleaning, cooking, nursing training.

Industry/Entity Type

Business

Contact Information for Business Card

Name: Marcus Liao
Chairman
Tel: 0574-57418263
Mobile: 13852247106
Email: kelvory@mailpond.com
Web: www.tqb2031.com

LOGO

Font styles to use
Serif
Sans Serif
Decorative

Requirements
Nice to have
• Feels: clean, specifications, safety, comfort, warmth and happiness.

```html
<!DOCTYPE html>
<html lang="en">
<head>
<meta charset="utf-8">
<title>Linwell Care Business Card</title>
<link href="https://fonts.googleapis.com/css2?family=Raleway:wght@400;500;700&display=swap" rel="stylesheet">
<style>
  :root{
    --bg:#bfe3da;
    --card:#ffffff;
    --blue:#0a7bc1;
    --blue-deep:#0b5fad;
    --pink:#e5098b;
    --ink:#1b6fb8;
  }
  *{box-sizing:border-box;margin:0;padding:0}
  html,body{width:1200px;height:856px;overflow:hidden}
  body{background:var(--bg);font-family:"Raleway",sans-serif;position:relative}
  .card{position:absolute;left:280px;width:640px;height:366px;background:var(--card);border-radius:34px;overflow:hidden;box-shadow:0 10px 24px rgba(0,60,50,.18)}
  .card--back{top:40px}
  .card--front{top:450px}
  .card svg.shapes{position:absolute;inset:0;width:100%;height:100%}
  .brand{position:absolute;display:flex;align-items:center;justify-content:center;gap:10px}
  .brand__mark{width:12px;height:12px;background:var(--blue-deep)}
  .brand__name{font-weight:700;font-size:34px;letter-spacing:.5px;color:var(--blue-deep);white-space:nowrap}
  .card--back .brand{left:0;right:0;top:158px}
  .card--front .brand{left:30px;width:270px;top:118px}
  .card--front .brand__name{font-size:28px}
  .address{position:absolute;left:30px;width:270px;top:226px;text-align:center;color:var(--ink);font-size:17px;line-height:1.4}
  .person{position:absolute;left:400px;top:62px;color:#fff}
  .person__name{font-size:27px;letter-spacing:1px;text-transform:uppercase;font-weight:400}
  .person__role{font-size:19px}
  .contacts{position:absolute;left:400px;top:190px;list-style:none;color:#fff;font-size:17px;line-height:1.55}
  .contacts li{display:flex;align-items:center;gap:10px}
  .contacts svg{width:17px;height:17px;flex:none}
</style>
</head>
<body>

<section class="card card--back" aria-label="Card back">
  <svg class="shapes" viewBox="0 0 640 366" aria-hidden="true">
    <rect x="0" y="326" width="640" height="40" fill="var(--blue)"/>
    <rect x="0" y="318" width="640" height="4" fill="var(--pink)"/>
  </svg>
  <div class="brand">
    <span class="brand__mark"></span><span class="brand__name">Linwell Care</span>
  </div>
</section>

<section class="card card--front" aria-label="Card front">
  <svg class="shapes" viewBox="0 0 640 366" aria-hidden="true">
    <path d="M300 0 Q300 250 430 366 L640 366 L640 0 Z" fill="var(--blue)"/>
    <path d="M284 0 Q284 262 410 366" fill="none" stroke="var(--blue)" stroke-width="4"/>
  </svg>
  <div class="brand">
    <span class="brand__mark"></span><span class="brand__name">Linwell Care</span>
  </div>
  <p class="address">No.258, LinfengJie<br>DaoyueQu, Ningbo, Zhejiang</p>
  <div class="person">
    <h1 class="person__name">Marcus Liao</h1>
    <p class="person__role">Chairman</p>
  </div>
  <ul class="contacts">
    <li><svg viewBox="0 0 20 20"><circle cx="10" cy="10" r="8.5" fill="none" stroke="#fff" stroke-width="1.5"/><path d="M7 5.5l2 2-1 1.2c.6 1.4 1.6 2.4 3 3l1.2-1 2 2-1.3 1.3c-3.3-.4-6.2-3.3-6.6-6.6z" fill="#fff"/></svg>0574-57418263</li>
    <li><svg viewBox="0 0 20 20"><rect x="5.5" y="2" width="9" height="16" rx="2" fill="none" stroke="#fff" stroke-width="1.5"/><circle cx="10" cy="15" r="1" fill="#fff"/></svg>13852247106</li>
    <li><svg viewBox="0 0 20 20"><rect x="2" y="4.5" width="16" height="11" fill="none" stroke="#fff" stroke-width="1.5"/><path d="M2 4.5l8 6 8-6" fill="none" stroke="#fff" stroke-width="1.5"/></svg>kelvory@mailpond.com</li>
    <li><svg viewBox="0 0 20 20"><circle cx="10" cy="10" r="8" fill="none" stroke="#fff" stroke-width="1.5"/><ellipse cx="10" cy="10" rx="3.5" ry="8" fill="none" stroke="#fff" stroke-width="1.2"/><path d="M2 10h16" stroke="#fff" stroke-width="1.2"/></svg>www.tqb2031.com</li>
  </ul>
</section>

</body>
</html>
```